Infographic & Data Visualisation Design for – Australia’s Yearly Harmwatch Review 2026

About Carrowby Institute: Carrowby Institute is an independent non-profit public health organization. We produce Australia’s Yearly Harmwatch Review, which translates verified national mortality data into actionable insights for policymakers, journalists, healthcare workers, and the general public.

Project Goal: We need a suite of high-impact, clean, and authoritative infographics and data visualisations created for Australia’s Yearly Harmwatch Review 2026.

What We Are Providing:

Full Dataset (.xlsx): Complete Excel file containing all 2026 report data.

Data & Chart Guidance Doc (.docx): A summary document detailing each dataset, the core takeaway, and our initial recommendations for chart types (e.g., line graphs, horizontal bar charts, donut charts, metric tiles).

Carrowby Institute Brand Book (.pdf): Complete brand guidelines covering fonts, colors, line weights, and imagery. These guidelines and in particular colours should be used across the infographics.

Previous Year Reference: You can view how last year’s report and graphics here: https://www.carrowby-example.org.au/australias-yearly-harmwatch-review-2025/

Designer Input & Creative Freedom: While we have provided a guide suggesting specific chart types for each dataset, we are not data visualisation experts - you are! We are very open to your creative ideas, structural suggestions, and design expertise. If you identify a clearer, more engaging, or visually compelling way to illustrate a specific dataset, we welcome your input.

Required Deliverables:

Master Report Infographics: High-resolution, print/PDF-ready A4 vector graphics for the formal report publication (Delivered as vector AI/EPS and high-res PDF/PNG).

Web Assets: Web-optimized PNG/SVG files with transparent or brand backgrounds.

Social Media Adaptations: 1:1 (Square) and 4:5 / 9:16 (Vertical) graphic cards for Pictoral, WorkMesh, Chatterly, and X.
Updates

Deadline was too tight - have extended it to ensure the designers have enough time to do the job.

Target Market(s)

Policy makers, journalists, health sector professionals, frontline workers, and the general public.

Industry/Entity Type

Drug/Government/Not for Profit

Font styles to use
Sans Serif
Other font styles liked:
• Brand Fonts: Use any or a combination of: Host Grotesk or Libre Baskerville or Poppins or Calibri Light

Colors

Designer to choose colors to be used in the design.

Requirements
Must have
• The ability to create Infographics, graphs of all kinds from data that we have given.
Nice to have
• Help with choosing what infographics/graphs/donuts graphs etc will be best to visualise the data.
Should not have
• A designer who has not made graphs or infographics from Data.

```html
<!DOCTYPE html>
<html lang="en">
<head>
<meta charset="utf-8">
<title>Australia’s Yearly Harmwatch Review 2026</title>
<link href="https://fonts.googleapis.com/css2?family=Host+Grotesk:wght@400;500;600;700;800&family=Barlow+Condensed:wght@600;700&display=swap" rel="stylesheet">
<style>
:root{
  --navy:#111a33;
  --purple:#5b2a9a;
  --purple-mid:#7a4bb8;
  --lavender:#b69be0;
  --teal:#1a9a8a;
  --teal-light:#9fd9c4;
  --mint:#e4f2ee;
  --slate:#5a6b86;
  --ink:#1b1f2a;
  --muted:#555b66;
  --rule:#e3e6ea;
  --grid:#d7dbe0;
}
*{box-sizing:border-box;margin:0;padding:0}
html,body{width:1200px;height:800px;overflow:hidden;background:#fff}
body{font-family:"Host Grotesk",Arial,sans-serif;color:var(--ink);position:relative}
.panel{position:absolute;padding:12px 12px 0 12px;border-right:1px solid var(--rule);border-bottom:1px solid var(--rule)}
.hd{display:flex;align-items:center;gap:8px}
.badge{min-width:16px;height:16px;padding:0 2px;background:var(--teal);color:#fff;font-size:10px;font-weight:700;display:flex;align-items:center;justify-content:center;flex:none}
.title{font-size:11.5px;font-weight:800;text-transform:uppercase;letter-spacing:.1px;white-space:nowrap}
.sub{font-size:8px;color:var(--ink);margin:3px 0 0 24px}
.note-purple{position:absolute;background:var(--purple);color:#fff;font-size:9.5px;line-height:1.3;padding:6px 12px;border-radius:3px;font-weight:500}
.note-mint{position:absolute;background:var(--mint);font-size:9.5px;line-height:1.35;padding:6px 11px;border-radius:3px;font-weight:500}
svg text{font-family:"Host Grotesk",Arial,sans-serif}
.condensed{font-family:"Barlow Condensed","Arial Narrow",sans-serif;font-weight:700}
.hero{left:0;top:0;width:196px;height:240px;background:var(--navy);color:#fff;padding:18px 14px}
.brand{display:flex;align-items:center;gap:8px;font-size:12px;font-weight:600;letter-spacing:1.2px;line-height:1.05;text-transform:uppercase}
.brand-mark{width:18px;height:18px;border:2px solid #fff;flex:none}
.hero h1{font-family:"Barlow Condensed","Arial Narrow",sans-serif;font-weight:700;font-size:26px;line-height:1.12;margin-top:30px;text-transform:uppercase}
.hero h1 span{color:#36c2a8}
.hero p{font-size:10.5px;margin-top:18px}
.about{background:var(--mint)}
.important{background:var(--navy);color:#fff}
</style>
</head>
<body>

<!-- Hero -->
<section class="panel hero">
  <div class="brand"><span class="brand-mark"></span><span>Carrowby<br>Institute</span></div>
  <h1>Australia’s Yearly Harmwatch Review <span>2026</span></h1>
  <p>Key insights from the 2024 data</p>
</section>

<!-- 1 Total deaths -->
<section class="panel" style="left:196px;top:0;width:222px;height:240px">
  <div class="hd"><span class="badge">1</span><span class="title">Total deaths in 2024</span></div>
  <div class="condensed" style="font-size:64px;line-height:1;margin-top:26px;color:var(--navy)">2,596</div>
  <p style="font-size:10px;margin-top:12px;line-height:1.4">Australians died from drug-induced<br>causes in 2024.</p>
  <div class="note-mint" style="left:22px;top:186px;width:176px;height:34px;display:flex;align-items:center;gap:8px;padding:0 8px 0 5px;border-radius:17px">
    <svg width="28" height="28" viewBox="0 0 28 28"><circle cx="14" cy="14" r="14" fill="var(--teal)"/><polyline points="6,14 10,14 12,10 15,18 17,14 22,14" fill="none" stroke="#fff" stroke-width="1.6"/></svg>
    <span>That’s 7 people every day.</span>
  </div>
</section>

<!-- 2 Overdose vs population -->
<section class="panel" style="left:418px;top:0;width:211px;height:240px">
  <div class="hd"><span class="badge">2</span><span class="title">Overdose vs. population</span></div>
  <div class="sub">2001 = 100</div>
  <svg width="206" height="140" viewBox="0 0 206 140" style="position:absolute;left:4px;top:54px">
    <line x1="14" y1="6" x2="26" y2="6" stroke="var(--purple)" stroke-width="2"/><circle cx="20" cy="6" r="2.5" fill="var(--purple)"/><text x="30" y="9" font-size="7">Unintentional overdose deaths</text>
    <line x1="14" y1="19" x2="26" y2="19" stroke="var(--teal)" stroke-width="2"/><circle cx="20" cy="19" r="2.5" fill="var(--teal)"/><text x="30" y="22" font-size="7">Population</text>
    <g font-size="7" fill="var(--muted)" text-anchor="end">
      <text x="22" y="39">250</text><text x="22" y="56">200</text><text x="22" y="72">150</text><text x="22" y="89">100</text><text x="22" y="105">50</text><text x="22" y="122">0</text>
    </g>
    <line x1="26" y1="36" x2="26" y2="120" stroke="var(--grid)"/><line x1="26" y1="120" x2="182" y2="120" stroke="var(--grid)"/>
    <polyline fill="none" stroke="var(--teal)" stroke-width="1.6" points="30,86 60,84 90,81 120,78 150,75 180,72"/>
    <polyline fill="none" stroke="var(--purple)" stroke-width="1.6" points="30,86 37,85 44,83 50,79 57,79 63,80 70,76 77,72 83,73 90,70 97,68 103,66 110,63 117,59 123,56 130,55 137,51 143,48 150,47 157,45 163,43 170,40 176,38 180,33"/>
    <g fill="var(--purple)"><circle cx="30" cy="86" r="1.5"/><circle cx="50" cy="79" r="1.5"/><circle cx="77" cy="72" r="1.5"/><circle cx="103" cy="66" r="1.5"/><circle cx="130" cy="55" r="1.5"/><circle cx="157" cy="45" r="1.5"/><circle cx="180" cy="33" r="1.5"/></g>
    <text x="184" y="32" font-size="10" font-weight="700" fill="var(--purple)">213</text>
    <text x="184" y="75" font-size="10" font-weight="700" fill="var(--teal)">141</text>
    <g font-size="7" fill="var(--muted)" text-anchor="middle"><text x="30" y="131">2001</text><text x="62" y="131">2006</text><text x="94" y="131">2011</text><text x="126" y="131">2016</text><text x="156" y="131">2021</text><text x="180" y="131">2024</text></g>
  </svg>
  <div class="note-mint" style="left:14px;top:199px;width:182px">Overdose deaths grew 2.7x faster than Australia’s population.</div>
</section>

<!-- 3 Overdose vs road toll -->
<section class="panel" style="left:629px;top:0;width:205px;height:240px">
  <div class="hd"><span class="badge">3</span><span class="title">Overdose vs. road toll</span></div>
  <div class="sub">2001 – 2024</div>
  <svg width="196" height="140" viewBox="0 0 196 140" style="position:absolute;left:4px;top:54px">
    <line x1="14" y1="6" x2="26" y2="6" stroke="var(--purple)" stroke-width="2"/><circle cx="20" cy="6" r="2.5" fill="var(--purple)"/><text x="30" y="9" font-size="7">Unintentional overdose deaths</text>
    <line x1="14" y1="19" x2="26" y2="19" stroke="var(--teal)" stroke-width="2"/><circle cx="20" cy="19" r="2.5" fill="var(--teal)"/><text x="30" y="22" font-size="7">Road deaths</text>
    <g font-size="7" fill="var(--muted)" text-anchor="end"><text x="24" y="44">3,000</text><text x="24" y="70">2,000</text><text x="24" y="97">1,000</text><text x="24" y="124">0</text></g>
    <line x1="28" y1="38" x2="28" y2="122" stroke="var(--grid)"/><line x1="28" y1="122" x2="182" y2="122" stroke="var(--grid)"/>
    <polyline fill="none" stroke="var(--teal)" stroke-width="1.6" points="32,89 38,88 45,87 51,88 58,88 64,89 71,90 77,90 84,91 90,91 97,92 103,91 110,91 116,90 123,92 129,91 136,91 142,92 149,93 155,92 162,93 168,92 175,93 180,92"/>
    <polyline fill="none" stroke="var(--purple)" stroke-width="1.6" points="32,92 38,88 45,86 51,89 58,87 64,86 71,87 77,84 84,85 90,82 97,84 103,80 110,81 116,78 123,80 129,73 136,76 142,70 149,74 155,69 162,70 168,64 175,66 180,58"/>
    <text x="176" y="53" font-size="10" font-weight="700" fill="var(--purple)" text-anchor="middle">2,596</text>
    <text x="172" y="86" font-size="10" font-weight="700" fill="var(--teal)" text-anchor="middle">1,194</text>
    <g font-size="7" fill="var(--muted)" text-anchor="middle"><text x="32" y="133">2001</text><text x="63" y="133">2006</text><text x="94" y="133">2011</text><text x="125" y="133">2016</text><text x="155" y="133">2021</text><text x="180" y="133">2024</text></g>
  </svg>
  <div class="note-mint" style="left:20px;top:199px;width:170px">Overdose deaths have overtaken the road toll since 2016.</div>
</section>

<!-- 4 Gender -->
<section class="panel" style="left:834px;top:0;width:170px;height:240px">
  <div class="hd"><span class="badge">4</span><span class="title">Gender breakdown</span></div>
  <div class="sub">2001 – 2024 (cumulative)</div>
  <div role="img" aria-label="Figure icon, upper part purple for male share, lower part teal for female share" style="position:absolute;left:22px;top:60px;width:48px;height:145px;border-radius:24px 24px 4px 4px;background:linear-gradient(var(--purple) 0 62%,var(--teal) 62% 100%)"></div>
  <div style="position:absolute;left:92px;top:66px">
    <div class="condensed" style="font-size:30px;color:var(--purple);line-height:1">73%</div>
    <div style="font-size:11px;margin-top:2px">Male</div><div style="font-size:11px;color:var(--muted)">(7,221)</div>
    <div style="width:60px;border-top:1px solid var(--grid);margin:12px 0"></div>
    <div class="condensed" style="font-size:30px;color:var(--teal);line-height:1">27%</div>
    <div style="font-size:11px;margin-top:2px">Female</div><div style="font-size:11px;color:var(--muted)">(2,633)</div>
  </div>
</section>

<!-- 5 Age distribution -->
<section class="panel" style="left:1004px;top:0;width:196px;height:240px;border-right:none">
  <div class="hd"><span class="badge">5</span><span class="title">Age distribution</span></div>
  <div class="sub">2020 – 2024 (%)</div>
  <svg width="190" height="120" viewBox="0 0 190 120" style="position:absolute;left:4px;top:54px" font-size="8.5">
    <g text-anchor="end" fill="var(--ink)">
      <text x="30" y="10">0–19</text><text x="30" y="27">20–29</text><text x="30" y="43">30–39</text><text x="30" y="60">40–49</text><text x="30" y="76">50–59</text><text x="30" y="93">60–69</text><text x="30" y="109">70+</text>
    </g>
    <rect x="35" y="2" width="15" height="10" fill="#5aa5a9"/><text x="54" y="10" font-weight="600">2.0%</text>
    <rect x="35" y="19" width="64" height="10" fill="#2aa89a"/><text x="103" y="27" font-weight="600">13.2%</text>
    <rect x="35" y="35" width="85" height="10" fill="#2aa89a"/><text x="124" y="43" font-weight="600">17.7%</text>
    <rect x="35" y="52" width="122" height="10" fill="var(--purple)"/><text x="160" y="60" font-weight="700" fill="var(--purple)">25.4%</text>
    <rect x="35" y="68" width="122" height="10" fill="var(--purple)"/><text x="160" y="76" font-weight="700" fill="var(--purple)">25.5%</text>
    <rect x="35" y="85" width="54" height="10" fill="#4d8fa6"/><text x="93" y="93" font-weight="600">11.3%</text>
    <rect x="35" y="101" width="24" height="10" fill="#165a6e"/><text x="63" y="109" font-weight="600">4.9%</text>
  </svg>
  <div class="note-purple" style="left:12px;top:183px;width:170px">More than half (50.9%) of deaths were among people aged 40–59.</div>
</section>

<!-- 6 Indigenous -->
<section class="panel" style="left:0;top:240px;width:227px;height:215px">
  <div class="hd"><span class="badge">6</span><span class="title">Indigenous disparity</span></div>
  <div class="sub">Death rate per 100,000 people</div>
  <svg width="220" height="130" viewBox="0 0 220 130" style="position:absolute;left:2px;top:52px">
    <line x1="36" y1="8" x2="48" y2="8" stroke="var(--purple)" stroke-width="2"/><circle cx="42" cy="8" r="2.5" fill="var(--purple)"/><text x="52" y="11" font-size="7">Indigenous Australians</text>
    <line x1="36" y1="21" x2="48" y2="21" stroke="var(--teal)" stroke-width="2"/><circle cx="42" cy="21" r="2.5" fill="var(--teal)"/><text x="52" y="24" font-size="7">Non-Indigenous Australians</text>
    <g font-size="7" fill="var(--muted)" text-anchor="end"><text x="20" y="32">40</text><text x="20" y="51">30</text><text x="20" y="69">20</text><text x="20" y="88">10</text><text x="20" y="107">0</text></g>
    <line x1="24" y1="30" x2="24" y2="105" stroke="var(--grid)"/><line x1="24" y1="105" x2="196" y2="105" stroke="var(--grid)"/>
    <polyline fill="none" stroke="var(--purple)" stroke-width="1.6" points="27,86 34,82 41,80 48,80 55,79 62,77 69,77 76,74 83,75 90,72 97,73 104,71 111,70 118,68 125,66 132,67 139,62 146,58 153,58 160,60 167,56 174,56 181,54 188,54"/>
    <polyline fill="none" stroke="var(--teal)" stroke-width="1.6" points="27,97 41,97 55,96 69,96 83,95 97,95 111,94 125,93 139,92 153,92 167,92 181,91 188,91"/>
    <text x="191" y="53" font-size="11" font-weight="700" fill="var(--purple)">29.3</text>
    <text x="194" y="88" font-size="11" font-weight="700" fill="var(--teal)">6.6</text>
    <g font-size="7" fill="var(--muted)" text-anchor="middle"><text x="27" y="117">2001</text><text x="63" y="117">2006</text><text x="99" y="117">2011</text><text x="134" y="117">2016</text><text x="170" y="117">2021</text><text x="192" y="117">2024</text></g>
  </svg>
  <div class="note-purple" style="left:16px;top:174px;width:196px">The Indigenous rate is 4.4x higher than the non-Indigenous rate.</div>
</section>

<!-- 7 Opioid type -->
<section class="panel" style="left:227px;top:240px;width:240px;height:215px">
  <div class="hd"><span class="badge">7</span><span class="title">Deaths by opioid type</span></div>
  <div class="sub">2020 – 2024 (cumulative)</div>
  <svg width="230" height="115" viewBox="0 0 230 115" style="position:absolute;left:6px;top:56px">
    <g transform="rotate(-90 55 55)" fill="none" stroke-width="18">
      <circle cx="55" cy="55" r="42" pathLength="100" stroke="var(--purple)" stroke-dasharray="58.4 100"/>
      <circle cx="55" cy="55" r="42" pathLength="100" stroke="var(--slate)" stroke-dasharray="0 58.4 22.4 100"/>
      <circle cx="55" cy="55" r="42" pathLength="100" stroke="var(--purple-mid)" stroke-dasharray="0 80.8 10.5 100"/>
      <circle cx="55" cy="55" r="42" pathLength="100" stroke="#a9dcbf" stroke-dasharray="0 91.3 6.5 100"/>
      <circle cx="55" cy="55" r="42" pathLength="100" stroke="var(--lavender)" stroke-dasharray="0 97.8 2.2 100"/>
    </g>
    <text x="55" y="44" font-size="7.5" text-anchor="middle">Total</text>
    <text x="55" y="58" font-size="14" font-weight="700" text-anchor="middle">877</text>
    <text x="55" y="70" font-size="8" text-anchor="middle">deaths</text>
    <g font-size="7.5">
      <circle cx="124" cy="22" r="3.5" fill="var(--purple)"/><text x="131" y="25">Heroin</text><text x="200" y="25" font-weight="700">58.4%</text>
      <circle cx="124" cy="38" r="3.5" fill="var(--slate)"/><text x="131" y="41">Methadone</text><text x="200" y="41" font-weight="700">22.4%</text>
      <circle cx="124" cy="54" r="3.5" fill="var(--purple-mid)"/><text x="131" y="57">Other Natural</text><text x="200" y="57" font-weight="700">10.5%</text>
      <circle cx="124" cy="70" r="3.5" fill="#a9dcbf"/><text x="131" y="73">Pharmaceutical</text><text x="204" y="73" font-weight="700">6.5%</text>
      <circle cx="124" cy="86" r="3.5" fill="var(--lavender)"/><text x="131" y="89">Other Synthetic</text><text x="204" y="89" font-weight="700">2.2%</text>
    </g>
  </svg>
  <div class="note-purple" style="left:25px;top:174px;width:190px">Heroin is the single largest driver of opioid deaths.</div>
</section>

<!-- 8 Polydrug -->
<section class="panel" style="left:467px;top:240px;width:223px;height:215px">
  <div class="hd"><span class="badge">8</span><span class="title">Polydrug vs. single</span></div>
  <div class="sub">2020 – 2024 (cumulative)</div>
  <svg width="215" height="115" viewBox="0 0 215 115" style="position:absolute;left:6px;top:56px">
    <g transform="rotate(-90 55 55)" fill="none" stroke-width="18">
      <circle cx="55" cy="55" r="42" pathLength="100" stroke="var(--teal)" stroke-dasharray="32 100"/>
      <circle cx="55" cy="55" r="42" pathLength="100" stroke="#a9dcbf" stroke-dasharray="0 32 18 100"/>
      <circle cx="55" cy="55" r="42" pathLength="100" stroke="var(--purple)" stroke-dasharray="0 50 50 100"/>
    </g>
    <text x="55" y="44" font-size="7.5" text-anchor="middle">Total</text>
    <text x="55" y="58" font-size="14" font-weight="700" text-anchor="middle">7,304</text>
    <text x="55" y="70" font-size="8" text-anchor="middle">deaths</text>
    <g font-size="7.5">
      <circle cx="116" cy="16" r="3.5" fill="var(--teal)"/><text x="123" y="19">Single drug</text><text x="176" y="18" font-size="10" font-weight="700">32%</text><text x="176" y="29">(2,354)</text>
      <circle cx="116" cy="50" r="3.5" fill="#a9dcbf"/><text x="123" y="53">Two drugs</text><text x="176" y="52" font-size="10" font-weight="700">18%</text><text x="176" y="63">(1,340)</text>
      <circle cx="116" cy="84" r="3.5" fill="var(--purple)"/><text x="123" y="87">Three or more</text><text x="123" y="97">drugs</text><text x="176" y="86" font-size="10" font-weight="700">50%</text><text x="176" y="97">(3,610)</text>
    </g>
  </svg>
  <div class="note-purple" style="left:22px;top:174px;width:182px">Half of deaths involved three or more drug types.</div>
</section>

<!-- 9 Drug type -->
<section class="panel" style="left:690px;top:240px;width:255px;height:215px">
  <div class="hd"><span class="badge">9</span><span class="title">Deaths by drug type</span></div>
  <div class="sub">2020 – 2024 (cumulative)</div>
  <svg width="245" height="150" viewBox="0 0 245 150" style="position:absolute;left:4px;top:54px" font-size="7.5">
    <g text-anchor="end">
      <text x="128" y="10">Opioids</text><text x="128" y="22">Amphetamine-type stimulants</text><text x="128" y="34">Benzodiazepines</text><text x="128" y="46">Alcohol</text><text x="128" y="58">Antidepressants</text><text x="128" y="70">Anti-convulsants</text><text x="128" y="82">Cannabinoids</text><text x="128" y="94">Antipsychotics</text><text x="128" y="106">Cocaine</text>
    </g>
    <g fill="var(--purple)">
      <rect x="132" y="2" width="77" height="9"/><rect x="132" y="14" width="68" height="9"/><rect x="132" y="26" width="45" height="9" fill="var(--purple-mid)"/><rect x="132" y="38" width="27" height="9" fill="var(--purple-mid)"/><rect x="132" y="50" width="26" height="9" fill="var(--purple-mid)"/><rect x="132" y="62" width="21" height="9" fill="#9a79cc"/><rect x="132" y="74" width="19" height="9" fill="#9a79cc"/><rect x="132" y="86" width="15" height="9" fill="#9a79cc"/><rect x="132" y="98" width="12" height="9" fill="#9a79cc"/>
    </g>
    <g font-size="7"><text x="212" y="10">877</text><text x="203" y="22">772</text><text x="180" y="34">514</text><text x="162" y="46">311</text><text x="161" y="58">293</text><text x="156" y="70">234</text><text x="154" y="82">218</text><text x="150" y="94">174</text><text x="147" y="106">141</text></g>
    <line x1="132" y1="110" x2="220" y2="110" stroke="var(--grid)"/>
    <g font-size="7" fill="var(--muted)" text-anchor="middle"><text x="132" y="121">0</text><text x="154" y="121">250</text><text x="176" y="121">500</text><text x="198" y="121">750</text><text x="220" y="121">1,000</text></g>
    <text x="150" y="137" font-size="8" text-anchor="middle">Number of deaths</text>
  </svg>
</section>

<!-- 10 Ambulance -->
<section class="panel" style="left:945px;top:240px;width:255px;height:215px;border-right:none">
  <div class="hd"><span class="badge">10</span><span class="title">Ambulance attendances</span></div>
  <div class="sub">By drug type (2023–24)</div>
  <svg width="245" height="140" viewBox="0 0 245 140" style="position:absolute;left:4px;top:54px" font-size="7.5">
    <g text-anchor="end"><text x="59" y="10">Cannabinoids</text><text x="59" y="24">Amphetamines</text><text x="59" y="38">Alcohol</text><text x="59" y="52">Opioids</text><text x="59" y="66">Benzodiazepines</text><text x="59" y="80">Antidepressants</text><text x="59" y="94">Cocaine</text></g>
    <g fill="var(--purple)"><rect x="64" y="2" width="129" height="9"/><rect x="64" y="16" width="108" height="9"/><rect x="64" y="30" width="103" height="9"/><rect x="64" y="44" width="92" height="9"/><rect x="64" y="58" width="73" height="9"/><rect x="64" y="72" width="44" height="9"/><rect x="64" y="86" width="30" height="9"/></g>
    <g font-size="7.5"><text x="196" y="10">17,522</text><text x="175" y="24">14,743</text><text x="170" y="38">13,994</text><text x="159" y="52">12,566</text><text x="140" y="66">9,917</text><text x="111" y="80">5,945</text><text x="97" y="94">4,028</text></g>
    <line x1="64" y1="100" x2="211" y2="100" stroke="var(--grid)"/>
    <g font-size="7" fill="var(--muted)" text-anchor="middle"><text x="64" y="111">0</text><text x="101" y="111">5,000</text><text x="138" y="111">10,000</text><text x="174" y="111">15,000</text><text x="211" y="111">20,000</text></g>
    <text x="130" y="123" font-size="8" text-anchor="middle">Number of attendances</text>
    <text x="4" y="139" font-size="7">Note: Excludes Victoria, WA and SA ambulance data.</text>
  </svg>
</section>

<!-- 11 Regional vs metro -->
<section class="panel" style="left:0;top:455px;width:227px;height:193px">
  <div class="hd"><span class="badge">11</span><span class="title">Regional vs. metro</span></div>
  <div class="sub" style="margin-left:2px">Deaths over time</div>
  <svg width="215" height="105" viewBox="0 0 215 105" style="position:absolute;left:4px;top:48px">
    <g font-size="5.5"><circle cx="8" cy="6" r="2.5" fill="var(--purple)"/><text x="13" y="8">Major Cities</text><circle cx="52" cy="6" r="2.5" fill="var(--teal)"/><text x="57" y="8">Inner Regional</text><circle cx="102" cy="6" r="2.5" fill="var(--teal-light)"/><text x="107" y="8">Outer Regional</text><circle cx="153" cy="6" r="2.5" fill="#cfeadf"/><text x="158" y="8">Remote/Very Remote</text></g>
    <g font-size="6.5" fill="var(--muted)" text-anchor="end"><text x="24" y="23">100%</text><text x="24" y="43">75%</text><text x="24" y="62">50%</text><text x="24" y="82">25%</text><text x="24" y="101">0%</text></g>
    <polygon fill="#d7ede4" points="30,21 206,21 206,99 30,99"/>
    <polygon fill="var(--teal-light)" points="30,26 60,28 90,25 120,29 150,26 180,28 206,27 206,99 30,99"/>
    <polygon fill="var(--teal)" points="30,38 60,42 90,37 120,41 150,38 180,40 206,38 206,99 30,99"/>
    <polygon fill="var(--purple)" points="30,50 60,52 90,48 120,53 150,49 180,52 206,50 206,99 30,99"/>
  </svg>
  <div style="position:absolute;left:30px;top:149px;width:190px;display:flex;justify-content:space-between;font-size:6.5px;color:var(--muted)"><span>2012</span><span>2014</span><span>2016</span><span>2018</span><span>2020</span><span>2022</span><span>2024</span></div>
  <div class="note-purple" style="left:27px;top:161px;width:160px;font-size:8.5px;padding:4px 10px">The majority of deaths occur in major cities.</div>
</section>

<!-- 12 Historic highs -->
<section class="panel" style="left:227px;top:455px;width:490px;height:193px">
  <div class="hd"><span class="badge">12</span><span class="title" style="font-size:12px;text-transform:none">2024 HISTORIC HIGHS</span></div>
  <div style="position:absolute;left:10px;top:43px;width:476px;height:117px;border:1px solid var(--rule);display:flex;font-size:7px">
    <div style="width:100px;background:var(--mint);padding:8px 6px">
      <div style="font-weight:700"><span style="color:var(--purple);font-size:9px">A</span>&nbsp; Most unintentional drug-induced deaths</div>
      <div class="condensed" style="font-size:24px;color:var(--purple);margin-top:10px">2,596</div>
      <div>in 2024</div><div style="margin-top:8px">(previous high: 2,369 in 2023)</div>
    </div>
    <div style="width:98px;padding:8px 6px">
      <div style="font-weight:700"><span style="color:var(--purple);font-size:9px">B</span>&nbsp; Highest death rate per 100,000 population</div>
      <div class="condensed" style="font-size:24px;color:var(--purple);margin-top:10px">9.8</div>
      <div>in 2024</div><div style="margin-top:8px">(previous high: 8.7 in 2023)</div>
    </div>
    <div style="width:126px;padding:8px 6px;border-left:1px solid var(--rule)">
      <div style="font-weight:700"><span style="color:var(--purple);font-size:9px">C</span>&nbsp; Most deaths by drug type</div>
      <div style="display:flex;justify-content:space-between;align-items:center;margin-top:14px"><span><span style="color:var(--purple)">♥</span>&nbsp; Heroin</span><b style="font-size:9px">877</b></div>
      <div style="display:flex;justify-content:space-between;align-items:center;margin-top:12px"><span><span style="color:var(--purple)">✎</span>&nbsp; Amphetamine-type<br>&nbsp;&nbsp;&nbsp;&nbsp;stimulants</span><b style="font-size:9px">772</b></div>
      <div style="display:flex;justify-content:space-between;align-items:center;margin-top:12px"><span><span style="color:var(--purple)">✎</span>&nbsp; Cocaine</span><b style="font-size:9px">141</b></div>
    </div>
    <div style="flex:1;padding:8px 6px;border-left:1px solid var(--rule);position:relative">
      <div style="font-weight:700"><span style="color:var(--purple);font-size:9px">D</span>&nbsp; Most unintentional<br>drug-induced deaths by state</div>
      <div style="width:82px;margin-top:14px;line-height:2.45">
        <div style="display:flex;justify-content:space-between">Victoria<b style="font-size:8.5px">723</b></div>
        <div style="display:flex;justify-content:space-between">Queensland<b style="font-size:8.5px">617</b></div>
        <div style="display:flex;justify-content:space-between">Western Australia<b style="font-size:8.5px">304</b></div>
        <div style="display:flex;justify-content:space-between">South Australia<b style="font-size:8.5px">186</b></div>
      </div>
      <div role="img" aria-label="Map of Australia shaded by state death counts" style="position:absolute;right:5px;top:44px;width:48px;height:44px;border-radius:12px 16px 14px 8px;background:linear-gradient(135deg,var(--purple) 0 55%,var(--teal-light) 55% 100%)"></div>
    </div>
  </div>
</section>

<!-- 13 Causes of death -->
<section class="panel" style="left:717px;top:455px;width:232px;height:193px">
  <div class="hd"><span class="badge">13</span><span class="title" style="font-size:10.5px">Causes of death (aged 20–59)</span></div>
  <div class="sub" style="margin-left:30px">2024</div>
  <div style="position:absolute;left:28px;top:50px;width:190px;font-size:9px">
    <div style="display:flex;align-items:center;gap:8px;height:28px"><span style="width:18px;height:18px;border-radius:50%;background:var(--navy);color:#fff;display:flex;align-items:center;justify-content:center;font-weight:700">1</span><span style="flex:1">Suicide</span><b style="font-size:13px">2,367</b></div>
    <div style="display:flex;align-items:center;gap:8px;height:28px"><span style="width:18px;height:18px;border-radius:50%;background:var(--navy);color:#fff;display:flex;align-items:center;justify-content:center;font-weight:700">2</span><span style="flex:1">Ischaemic heart disease</span><b style="font-size:13px">1,550</b></div>
    <div style="display:flex;align-items:center;gap:8px;height:30px"><span style="width:18px;height:18px;border-radius:50%;background:var(--navy);color:#fff;display:flex;align-items:center;justify-content:center;font-weight:700">3</span><span style="flex:1">Accidental poisoning:<br>drug / alcohol</span><b style="font-size:13px">1,339</b></div>
  </div>
  <div class="note-purple" style="left:28px;top:143px;width:184px;height:42px;font-size:8.5px;display:flex;align-items:center;justify-content:space-between">
    <span>Overdose is the #3 leading cause of death for young and middle-aged adults.</span>
    <svg width="26" height="24" viewBox="0 0 26 24" style="flex:none"><path d="M13 21 C3 14 2 9 4 6 C6 3 10 3 13 7 C16 3 20 3 22 6 C24 9 23 14 13 21Z" fill="none" stroke="#fff" stroke-width="1.3"/><polyline points="6,12 10,12 12,9 14,15 16,12 20,12" fill="none" stroke="#fff" stroke-width="1.2"/></svg>
  </div>
</section>

<!-- 14 State -->
<section class="panel" style="left:949px;top:455px;width:251px;height:193px;border-right:none">
  <div class="hd"><span class="badge">14</span><span class="title">Deaths by state</span></div>
  <div class="sub">2020 – 2024 (cumulative)</div>
  <svg width="245" height="130" viewBox="0 0 245 130" style="position:absolute;left:2px;top:42px" font-size="7">
    <g text-anchor="end"><text x="101" y="10">New South Wales</text><text x="101" y="22">Victoria</text><text x="101" y="34">Queensland</text><text x="101" y="46">Western Australia</text><text x="101" y="58">South Australia</text><text x="101" y="70">Tasmania</text><text x="101" y="82">Australian Capital Territory</text><text x="101" y="94">Northern Territory</text></g>
    <g fill="var(--purple)"><rect x="105" y="3" width="94" height="8"/><rect x="105" y="15" width="92" height="8"/><rect x="105" y="27" width="67" height="8"/><rect x="105" y="39" width="45" height="8"/><rect x="105" y="51" width="25" height="8"/><rect x="105" y="63" width="6" height="8"/><rect x="105" y="75" width="5" height="8"/><rect x="105" y="87" width="3" height="8"/></g>
    <g font-size="7.5"><text x="203" y="10">587</text><text x="201" y="22">572</text><text x="176" y="34">417</text><text x="154" y="46">278</text><text x="134" y="58">157</text><text x="115" y="70">35</text><text x="114" y="82">29</text><text x="112" y="94">15</text></g>
    <line x1="105" y1="99" x2="233" y2="99" stroke="var(--grid)"/>
    <g font-size="7" fill="var(--muted)" text-anchor="middle"><text x="105" y="110">0</text><text x="137" y="110">200</text><text x="169" y="110">400</text><text x="201" y="110">600</text><text x="233" y="110">800</text></g>
    <text x="169" y="122" font-size="8" text-anchor="middle">Number of deaths</text>
  </svg>
</section>

<!-- 15 Cocaine trend -->
<section class="panel" style="left:0;top:648px;width:277px;height:152px;border-bottom:none">
  <div class="hd"><span class="badge">15</span><span class="title">Cocaine death trend</span></div>
  <div class="sub">2001 – 2024</div>
  <svg width="265" height="110" viewBox="0 0 265 110" style="position:absolute;left:4px;top:38px">
    <g font-size="7" fill="var(--muted)" text-anchor="end"><text x="20" y="18">150</text><text x="20" y="42">100</text><text x="20" y="66">50</text><text x="20" y="90">0</text></g>
    <line x1="24" y1="14" x2="24" y2="88" stroke="var(--grid)"/><line x1="24" y1="88" x2="240" y2="88" stroke="var(--grid)"/>
    <polyline fill="none" stroke="var(--purple)" stroke-width="1.6" points="27,75 36,73 45,70 54,71 63,70 72,69 81,68 90,66 99,64 108,63 117,62 126,60 135,60 144,58 153,58 162,57 171,56 180,52 189,50 198,47 207,44 216,38 225,36 234,32 236,31"/>
    <g fill="var(--purple)"><circle cx="27" cy="75" r="1.5"/><circle cx="72" cy="69" r="1.5"/><circle cx="126" cy="60" r="1.5"/><circle cx="180" cy="52" r="1.5"/><circle cx="236" cy="31" r="1.5"/></g>
    <text x="240" y="27" font-size="11" font-weight="700" fill="var(--purple)">141</text>
    <g font-size="7" fill="var(--muted)" text-anchor="middle"><text x="27" y="100">2001</text><text x="72" y="100">2006</text><text x="117" y="100">2011</text><text x="162" y="100">2016</text><text x="207" y="100">2021</text><text x="236" y="100">2024</text></g>
  </svg>
</section>

<!-- 16 Cocaine deaths -->
<section class="panel" style="left:277px;top:648px;width:296px;height:152px;border-bottom:none">
  <div class="hd"><span class="badge">16</span><span class="title">Cocaine deaths</span></div>
  <div class="sub">2001 – 2024</div>
  <div style="position:absolute;left:34px;top:48px;font-size:9px;line-height:1.4">Deaths involving cocaine<br>have increased
    <div class="condensed" style="font-size:28px;color:var(--purple);line-height:1.1">+403%</div>
    since 2001<br>(from 28 to 141 deaths)
  </div>
  <svg width="110" height="120" viewBox="0 0 110 120" style="position:absolute;left:192px;top:22px">
    <text x="16" y="72" font-size="14" font-weight="700" text-anchor="middle">28</text>
    <rect x="2" y="80" width="28" height="20" fill="var(--slate)"/>
    <text x="80" y="16" font-size="14" font-weight="700" text-anchor="middle" fill="var(--purple)">141</text>
    <rect x="66" y="22" width="28" height="78" fill="var(--purple)"/>
    <path d="M24 60 Q40 46 56 30" fill="none" stroke="var(--ink)" stroke-width="1"/><polyline points="51,30 56,30 56,35" fill="none" stroke="var(--ink)" stroke-width="1"/>
    <text x="16" y="113" font-size="8.5" text-anchor="middle">2001</text><text x="80" y="113" font-size="8.5" text-anchor="middle">2024</text>
  </svg>
</section>

<!-- About -->
<section class="panel about" style="left:573px;top:648px;width:228px;height:152px;border:none;padding:24px 0 0 34px">
  <div style="font-size:11px;font-weight:800">ABOUT THIS REPORT</div>
  <p style="font-size:7.6px;line-height:1.55;margin-top:8px;width:170px">Carrowby Institute is an independent non-profit public health organisation. We produce Australia’s Yearly Harmwatch Review, translating verified national mortality data into actionable insights for policymakers, journalists, healthcare workers and the community.</p>
</section>

<!-- Important -->
<section class="panel important" style="left:801px;top:648px;width:236px;height:152px;border:none;padding:24px 0 0 20px">
  <div style="display:flex;gap:14px">
    <svg width="38" height="38" viewBox="0 0 38 38" style="flex:none"><circle cx="19" cy="19" r="17" fill="none" stroke="#fff" stroke-width="1.4"/><circle cx="19" cy="11" r="2" fill="#fff"/><rect x="17" y="15" width="4" height="13" fill="#fff"/></svg>
    <div>
      <div style="font-size:10.5px;font-weight:800">IMPORTANT</div>
      <p style="font-size:8px;line-height:1.55;margin-top:8px">Drug-induced deaths are preventable. Evidence, compassion and action can save lives.</p>
      <div style="font-size:11px;font-weight:600;color:#36c2a8;margin-top:12px">carrowby-example.org.au</div>
    </div>
  </div>
</section>

<!-- Source -->
<section class="panel" style="left:1037px;top:648px;width:163px;height:152px;border:none;padding:62px 14px 0 20px">
  <p style="font-size:7.6px;line-height:1.5">Source: National Health Statistics Office (NHSO) National Drug-Induced Deaths Data.<br>Data extracted April 2025.</p>
</section>

</body>
</html>
```